Business Card Design Project

2 sided business card utilizing existing logo
- English on one side, Arabic on the other side (both English and Arabic text will be provided)
Same color scheme as logo
Information included will be: name, title, email, phone, address and website (www.veralunix.com)
Updates

Target Market(s)

We are a Systems Integration Company

Industry/Entity Type

Business

Font styles to use
Serif
Sans Serif

Requirements
Should not have
• We prefer using the flat logo rather than one with shadow/3D effect

```html
<!DOCTYPE html>
<html lang="en">
<head>
<meta charset="utf-8">
<title>Veralunix – Business Card</title>
<link rel="stylesheet" href="https://fonts.googleapis.com/css2?family=Source+Sans+3:wght@300;400;600&display=swap">
<style>
  :root {
    --backdrop: #444341;
    --card-red: #e9272b;
    --ink-white: #ffffff;
  }
  * { margin: 0; padding: 0; box-sizing: border-box; }
  html, body {
    width: 1200px;
    height: 900px;
    overflow: hidden;
    background: var(--backdrop);
    font-family: "Source Sans 3", "Helvetica Neue", Arial, sans-serif;
    color: var(--ink-white);
  }
  .canvas {
    position: relative;
    width: 1200px;
    height: 900px;
  }
  .card-shape {
    position: absolute;
    left: 0;
    top: 0;
  }
  .card-content {
    position: absolute;
    right: 481px;
    top: 0;
    width: 240px;
    text-align: right;
  }
  .line {
    position: absolute;
    right: 0;
    white-space: nowrap;
  }
  .brand-mark {
    position: absolute;
    right: 44px;
    top: 312px;
    width: 30px;
    height: 30px;
    background: var(--ink-white);
    transform: rotate(45deg);
  }
  .brand-name {
    top: 378px;
    font-size: 17px;
    font-weight: 600;
    letter-spacing: 4px;
    line-height: 20px;
    margin-right: -4px;
  }
  .person-name {
    top: 421px;
    font-size: 40px;
    font-weight: 300;
    line-height: 46px;
  }
  .person-title {
    top: 467px;
    font-size: 15px;
    font-weight: 400;
    line-height: 18px;
  }
  .address-line-1 { top: 501px; }
  .address-line-2 { top: 520px; }
  .phone-office  { top: 553px; }
  .phone-mobile  { top: 574px; }
  .email         { top: 596px; }
  .website       { top: 629px; }
  .detail {
    font-size: 15px;
    font-weight: 400;
    line-height: 18px;
    display: flex;
    align-items: center;
    gap: 6px;
  }
  .detail svg { display: block; }
</style>
</head>
<body>
  <main class="canvas">
    <svg class="card-shape" width="1200" height="900" viewBox="0 0 1200 900" aria-hidden="true">
      <path d="M467.5 208.5 H700 Q705 208.5 709 212 L751.5 255 V690 H520 Q515 690 511 686.5 L467.5 643.5 Z" fill="var(--card-red)"/>
    </svg>

    <section class="card-content">
      <div class="brand-mark" aria-hidden="true"></div>
      <div class="line brand-name">VERALUNIX</div>

      <h1 class="line person-name">John Doe</h1>
      <p class="line person-title">Creative Director</p>

      <p class="line detail address-line-1">27 Ipsum Lane</p>
      <p class="line detail address-line-2">Fairholt, Michigan, 90311</p>

      <p class="line detail phone-office">
        <svg width="17" height="12" viewBox="0 0 17 12" aria-hidden="true">
          <path d="M1 4 Q8.5 -1 16 4 L14 6 L11.5 4.5 V3.5 H5.5 V4.5 L3 6 Z" fill="var(--ink-white)"/>
          <path d="M4 6 H13 L14.5 11.5 H2.5 Z" fill="var(--ink-white)"/>
          <circle cx="8.5" cy="8.5" r="1.6" fill="var(--card-red)"/>
        </svg>
        +001 555 0134 218
      </p>
      <p class="line detail phone-mobile">
        <svg width="10" height="15" viewBox="0 0 10 15" aria-hidden="true">
          <rect x="0.5" y="2" width="9" height="12.5" rx="2" fill="var(--ink-white)"/>
          <rect x="2" y="0" width="1.5" height="3" fill="var(--ink-white)"/>
          <rect x="2.3" y="4" width="5.4" height="4" fill="var(--card-red)"/>
        </svg>
        +001 555 0198 4470
      </p>
      <p class="line detail email">
        <svg width="18" height="12" viewBox="0 0 18 12" aria-hidden="true">
          <rect x="0.75" y="0.75" width="16.5" height="10.5" fill="none" stroke="var(--ink-white)" stroke-width="1.5"/>
          <path d="M1 1 L9 7 L17 1 M1 11 L7 5.5 M17 11 L11 5.5" fill="none" stroke="var(--ink-white)" stroke-width="1.3"/>
        </svg>
        john@veralunix.com
      </p>

      <p class="line detail website">www.veralunix.com</p>
    </section>
  </main>
</body>
</html>
```